International Food Company needs packaging design for new products

We have a logo for our new business. It is attached. Now we need a packaging design for the products that we will be selling. We are an international wholesale foods company selling foods and herbs that will be certified organic and Non-GMO imported from West Africa. We are just in the process of launching new products. We're looking for a design that is fresh and modern.

Here is a list of items that we are requesting packaging design for.

Baobob Powder-8 oz and 12 oz
Dried Mango- 8 oz
Mango Powder 8 oz and 12 oz

```html
<!DOCTYPE html>
<html lang="en">
<head>
<meta charset="utf-8">
<title>Sunvale Herbs – Packaging Range</title>
<link rel="stylesheet" href="https://fonts.googleapis.com/css2?family=Jost:wght@400;500&family=Cabin:wght@500&display=swap">
<style>
  :root {
    --bg: #eeeeee;
    --ink: #141414;
    --black: #161616;
    --mango: #f3b220;
    --baobab: #cdbf9e;
    --paper: #ebe8e2;
    --orange: #e8862a;
    --brand-green: #33b37c;
    --badge-green: #2f9e4b;
  }
  * { box-sizing: border-box; margin: 0; padding: 0; }
  html, body { width: 1200px; height: 800px; overflow: hidden; }
  body {
    background: var(--bg);
    position: relative;
    font-family: "Jost", Arial, sans-serif;
    color: var(--ink);
    line-height: 1.2;
  }

  .pack { position: absolute; background: var(--black); overflow: hidden; }
  .pouch { left: 133px; top: 75px; width: 353px; height: 590px; border-radius: 4px; --accent: var(--mango); }
  .jar-label { top: 252px; width: 189px; height: 400px; }
  .jar-label.baobab { left: 600px; --accent: var(--baobab); }
  .jar-label.mango { left: 906px; --accent: var(--mango); }

  .hang-hole {
    position: absolute; left: 131px; top: 30px; width: 98px; height: 22px;
    background: var(--bg); border-radius: 11px;
  }
  .zip-line {
    position: absolute; left: 18px; right: 18px; top: 58px; height: 2px;
    background: #2c2c2c;
  }

  .brand {
    position: absolute; left: 0; right: 0;
    display: flex; justify-content: center; align-items: center; gap: 8px;
    color: var(--brand-green); font-weight: 400; letter-spacing: 1px;
    text-transform: uppercase; white-space: nowrap;
  }
  .brand-dot { border-radius: 50%; background: var(--brand-green); }
  .pouch .brand { top: 150px; font-size: 25px; }
  .pouch .brand-dot { width: 14px; height: 14px; }
  .jar-label .brand { top: 95px; font-size: 19px; }
  .jar-label .brand-dot { width: 11px; height: 11px; }

  .paper { position: absolute; left: 0; right: 0; background: var(--paper); }
  .pouch .paper { top: 270px; height: 265px; }
  .jar-label .paper { top: 175px; height: 200px; }

  .title-band {
    position: absolute; left: 0; right: 0; background: var(--accent);
    text-align: center;
    clip-path: polygon(0 10%, 8% 6%, 18% 11%, 30% 4%, 44% 9%, 58% 3%, 72% 8%, 86% 2%, 100% 6%,
                       100% 88%, 88% 94%, 74% 89%, 60% 97%, 46% 91%, 32% 98%, 18% 92%, 6% 99%, 0 94%);
  }
  .pouch .title-band { top: 215px; height: 77px; padding-top: 14px; }
  .jar-label .title-band { top: 142px; height: 62px; padding-top: 13px; }

  .title-organic { display: block; font-weight: 400; line-height: 1; }
  .title-product { display: block; font-weight: 500; line-height: 1.05; text-transform: uppercase; white-space: nowrap; }
  .pouch .title-organic { font-size: 19px; }
  .pouch .title-product { font-size: 28px; margin-top: 3px; }
  .jar-label .title-organic { font-size: 13px; }
  .jar-label .title-product { font-size: 17px; margin-top: 2px; }

  .origin {
    position: absolute; left: 0; right: 0; text-align: center;
    font-family: "Cabin", Arial, sans-serif; font-weight: 500; color: var(--orange);
  }
  .pouch .origin { top: 290px; font-size: 14px; }
  .jar-label .origin { top: 212px; font-size: 12px; line-height: 1.15; }

  .artwork { position: absolute; border-radius: 40% 50% 45% 40%; }
  .artwork.mango-art {
    background: radial-gradient(ellipse at 40% 55%, #f4e13a 0%, #f2b826 45%, #e88a3a 75%, rgba(235,232,226,0) 100%);
  }
  .artwork.baobab-art {
    background: radial-gradient(ellipse at 40% 55%, #e9dcc4 0%, #b48a5f 50%, #9a8f6f 75%, rgba(235,232,226,0) 100%);
  }
  .pouch .artwork { left: 35px; top: 310px; width: 300px; height: 185px; }
  .jar-label .artwork { left: 8px; top: 246px; width: 140px; height: 92px; }

  .badge { position: absolute; border-radius: 50%; border: 3px solid var(--badge-green); }
  .pouch .badge { left: 252px; top: 468px; width: 54px; height: 54px; }
  .jar-label .badge { left: 146px; top: 294px; width: 38px; height: 38px; border-width: 2px; }

  .net-weight { position: absolute; font-weight: 500; text-transform: uppercase; white-space: nowrap; }
  .pouch .net-weight { left: 32px; top: 505px; font-size: 17px; }
  .jar-label .net-weight { left: 0; right: 0; text-align: center; top: 347px; font-size: 14px; }

  .accent-line { position: absolute; left: 0; right: 0; background: var(--accent); }
  .pouch .accent-line { top: 535px; height: 8px; }
  .jar-label .accent-line { top: 375px; height: 5px; }
</style>
</head>
<body>

  <section class="pack pouch" aria-label="Dried mango pouch">
    <div class="hang-hole"></div>
    <div class="zip-line"></div>
    <div class="brand"><span class="brand-dot"></span>Sunvale Herbs</div>
    <div class="paper"></div>
    <div class="title-band">
      <span class="title-organic">ORGANIC</span>
      <span class="title-product">Dried Mango</span>
    </div>
    <p class="origin">Imported from West Africa</p>
    <div class="artwork mango-art" role="img" aria-label="Watercolour illustration of dried mango slices"></div>
    <div class="badge"></div>
    <p class="net-weight">Net Wt 8 oz</p>
    <div class="accent-line"></div>
  </section>

  <section class="pack jar-label baobab" aria-label="Baobab powder jar label">
    <div class="brand"><span class="brand-dot"></span>Sunvale Herbs</div>
    <div class="paper"></div>
    <div class="title-band">
      <span class="title-organic">ORGANIC</span>
      <span class="title-product">Baobob Powder</span>
    </div>
    <p class="origin">Imported from<br>West Africa</p>
    <div class="artwork baobab-art" role="img" aria-label="Illustration of an opened baobab fruit"></div>
    <div class="badge"></div>
    <p class="net-weight">Net Wt 8 oz</p>
    <div class="accent-line"></div>
  </section>

  <section class="pack jar-label mango" aria-label="Mango powder jar label">
    <div class="brand"><span class="brand-dot"></span>Sunvale Herbs</div>
    <div class="paper"></div>
    <div class="title-band">
      <span class="title-organic">ORGANIC</span>
      <span class="title-product">Mango Powder</span>
    </div>
    <p class="origin">Imported from<br>West Africa</p>
    <div class="artwork mango-art" role="img" aria-label="Watercolour illustration of mango slices"></div>
    <div class="badge"></div>
    <p class="net-weight">Net Wt 8 oz</p>
    <div class="accent-line"></div>
  </section>

</body>
</html>
```